Mortgage Broking Business needs a 1 page single sided 'brochure / flyer

I require a one page single sided 'brochure / flyer' that i can 1. Email to potential clients (Limited MB so easily emailed) and 2. Print and post to potential clients. (A4) High resolution color. I think both should be Landscape format.
Look at my website www.pebblecrestloans.com.au to find inspiration - clear / clean / crisp / blue tones

Target Market(s)

Potential borrowers - age 25 to 50 for home and Investment Loans

Industry/Entity Type

Finance

Font styles to use
Sans Serif

Colors
33a6d7
0692cd

Requirements
Must have
• Must Include:
• -My Headshot
• -Company Logo
• -Lenders Logos - can cut and paste from my affiliate website http://www.harbornestlending.com.au/index.php?page=preferredpartners
• - Tag Line - Smart Lending Solutions Sydney Australia
• - Service Offering
Nice to have
• Lightbulb as per website
Should not have
• Should not look cluttered

```html
<!DOCTYPE html>
<html lang="en">
<head>
<meta charset="utf-8">
<title>Pebblecrest Home Loans – Smart Lending Solutions Flyer</title>
<link href="https://fonts.googleapis.com/css2?family=Oswald:wght@600;700&family=Open+Sans:wght@400;600;700&family=Arimo:wght@400&display=swap" rel="stylesheet">
<style>
  :root {
    --brand-blue: #33a6d7;
    --brand-blue-deep: #0692cd;
    --blue-shade: #1d6f9a;
    --ink: #222628;
    --ink-soft: #5a5e62;
    --ribbon: #3b3f43;
    --paper: #ffffff;
    --logo-grey: #9bb2c4;
  }
  * { margin: 0; padding: 0; box-sizing: border-box; }
  html, body { width: 1200px; height: 888px; overflow: hidden; background: var(--paper); }
  .flyer {
    position: relative; width: 1200px; height: 888px; overflow: hidden;
    background: linear-gradient(170deg, #ffffff 0%, #f4f5f7 55%, #ffffff 100%);
    font-family: "Open Sans", Arial, sans-serif; color: var(--ink);
  }
  .backdrop { position: absolute; inset: 0; }

  .brand-name {
    position: absolute; left: 818px; top: 84px;
    font-family: "Open Sans", Arial, sans-serif; font-weight: 400;
    font-size: 36px; line-height: 1.05; color: var(--logo-grey); letter-spacing: 0.5px;
  }
  .brand-name small { display: block; font-size: 17px; letter-spacing: 1px; }

  .headline {
    position: absolute; left: 475px; top: 286px; white-space: nowrap;
    font-family: "Oswald", Impact, sans-serif; font-weight: 700;
    font-size: 56px; line-height: 1.2; color: var(--brand-blue);
    text-shadow: 0 2px 2px rgba(0,0,0,0.15);
  }
  .headline-place {
    position: absolute; left: 478px; top: 374px; white-space: nowrap;
    font-family: "Arimo", Arial, sans-serif; font-size: 50px; line-height: 1;
    color: var(--ink-soft); letter-spacing: 18.5px;
  }

  .tag {
    position: absolute; height: 30px; white-space: nowrap;
    background: var(--ribbon);
    font-family: "Oswald", Impact, sans-serif; font-weight: 600;
    font-size: 21px; line-height: 30px; color: var(--brand-blue); letter-spacing: 0.3px;
  }
  .tag--left { left: 0; padding-left: 24px; clip-path: polygon(0 0, 100% 0, calc(100% - 16px) 100%, 0 100%); }
  .tag--right { right: 0; padding-left: 50px; clip-path: polygon(18px 0, 100% 0, 100% 100%, 0 100%); }
  .tag--services { top: 482px; width: 248px; }
  .tag--education { top: 679px; width: 332px; }
  .tag--experience { top: 461px; width: 218px; }

  .services-intro {
    position: absolute; left: 35px; top: 522px; width: 520px;
    font-size: 15px; line-height: 22px;
  }
  .ticks { list-style: none; }
  .ticks li { position: relative; padding-left: 16px; font-size: 15px; line-height: 22px; white-space: nowrap; }
  .ticks li::before {
    content: ""; position: absolute; left: 1px; top: 8px; width: 6px; height: 6px;
    border-top: 2px solid var(--brand-blue); border-right: 2px solid var(--brand-blue);
    transform: rotate(45deg);
  }
  .education-list { position: absolute; left: 35px; top: 722px; }

  .experience-copy {
    position: absolute; left: 638px; top: 520px; width: 527px;
    font-size: 15px; line-height: 22.4px; text-align: justify;
  }
  .divider {
    position: absolute; left: 594px; top: 520px; width: 3px; height: 78px;
    background: linear-gradient(#fff, #c9ccd0, #fff); border-radius: 2px;
  }

  .disclosure {
    position: absolute; left: 329px; top: 779px;
    color: #fff; font-size: 11px; font-weight: 700; line-height: 16px; white-space: nowrap;
  }

  .cta {
    position: absolute; left: 734px; top: 651px; width: 443px; height: 186px;
    background: var(--brand-blue); border-radius: 12px; color: #fff; overflow: hidden;
  }
  .cta-call {
    position: absolute; left: 44px; top: 0;
    font-family: "Oswald", Impact, sans-serif; font-weight: 700; font-size: 48px; line-height: 62px; white-space: nowrap;
  }
  .cta-band {
    position: absolute; left: 0; top: 62px; width: 100%; height: 40px; background: #fff;
    padding-left: 44px; white-space: nowrap;
    font-family: "Oswald", Impact, sans-serif; font-weight: 600; font-size: 31px; line-height: 40px;
    color: var(--ink);
  }
  .cta-name { position: absolute; left: 35px; top: 128px; font-size: 17px; font-weight: 600; letter-spacing: 0.3px; white-space: nowrap; }
  .cta-phone {
    position: absolute; left: 30px; top: 150px; display: flex; align-items: center; gap: 8px;
    font-size: 23px; font-weight: 600; line-height: 28px; white-space: nowrap;
  }
  .cta-address { position: absolute; left: 249px; top: 138px; font-size: 15px; line-height: 21px; white-space: nowrap; }

  .headshot {
    position: absolute; left: 553px; top: 606px; width: 214px; height: 214px; border-radius: 50%;
    background: #2c2f33; box-shadow: 0 3px 8px rgba(0,0,0,0.3);
  }
  .headshot-fill {
    position: absolute; inset: 9px; border-radius: 50%;
    background: radial-gradient(circle at 50% 40%, #e4b79e 0%, #c99a82 35%, #e58aa4 70%, #3a3d41 100%);
  }
</style>
</head>
<body>
<main class="flyer">
  <svg class="backdrop" width="1200" height="888" viewBox="0 0 1200 888" aria-hidden="true">
    <defs>
      <linearGradient id="photoTone" x1="0" y1="0" x2="1" y2="0.3">
        <stop offset="0" stop-color="#7a8796"/>
        <stop offset="0.5" stop-color="#aab5c1"/>
        <stop offset="1" stop-color="#f2f3f5"/>
      </linearGradient>
      <linearGradient id="mistTone" x1="0" y1="0" x2="1" y2="1">
        <stop offset="0" stop-color="#f6f7f8"/>
        <stop offset="1" stop-color="#dcdfe3"/>
      </linearGradient>
      <linearGradient id="bandTone" x1="0" y1="1" x2="1" y2="0">
        <stop offset="0" stop-color="#33a6d7"/>
        <stop offset="1" stop-color="#0692cd"/>
      </linearGradient>
    </defs>
    <polygon points="0,0 740,0 740,142 0,342" fill="url(#photoTone)" role="img" aria-label="Photo: business people shaking hands across a table in a bright office"/>
    <polygon points="700,0 1200,0 1200,312 740,140" fill="url(#mistTone)"/>
    <polygon points="0,342 740,142 760,150 0,428" fill="url(#bandTone)"/>
    <polygon points="122,405 745,150 760,150 146,458" fill="#2a9ad0"/>
    <polygon points="690,140 740,128 745,144 705,152" fill="#1f3b52"/>
    <polygon points="289,740 535,740 565,860 319,860" fill="var(--brand-blue-deep)"/>
    <polygon points="277,740 289,740 319,860 307,860" fill="var(--blue-shade)"/>
    <rect x="0" y="861" width="1200" height="27" fill="var(--brand-blue)"/>
  </svg>

  <div class="brand-name">Pebblecrest<small>Home Loans</small></div>

  <h1 class="headline">SMART LENDING SOLUTIONS</h1>
  <p class="headline-place">Sydney Australia</p>

  <h2 class="tag tag--left tag--services">SERVICES OFFERED:</h2>
  <div class="services-intro">
    <p>With over 40 Lenders and Preferred Partners on our Panel we can find a solution for you. Call us for all of your borrowing needs:</p>
    <ul class="ticks">
      <li>Refinance of existing loans to lower Interest rates</li>
      <li>Top Ups for renovations</li>
      <li>Purchase of Owner Occupied and Investment Property</li>
      <li>Purchase of Commercial Property</li>
    </ul>
  </div>

  <h2 class="tag tag--left tag--education">EDUCATION / QUALIFICATIONS</h2>
  <ul class="ticks education-list">
    <li>BComm EHU</li>
    <li>Dip Financial Planning</li>
    <li>Cert IV Mortgage Broking</li>
    <li>Justice of the Peace</li>
    <li>Member MLBA / FPN Affiliate</li>
  </ul>

  <div class="disclosure">
    <p>Disclosure:</p>
    <p>Pebblecrest Financial Services Pty Ltd<br>T/As Pebblecrest Home Loans<br>Australian Credit Licence No: 400123</p>
  </div>

  <h2 class="tag tag--right tag--experience">EXPERIENCE:</h2>
  <div class="divider" aria-hidden="true"></div>
  <p class="experience-copy">Sam Whitford-Lane has been working in the Finance Industry for over 20 years. With a background in Accounting, Banking, Financial Planning and Mortgage Broking Sam brings a wealth of knowledge and experience to assist with all of your Finance needs.</p>

  <section class="cta">
    <p class="cta-call">CALL SAM NOW TO</p>
    <p class="cta-band">discuss your borrowing needs</p>
    <p class="cta-name">SAM WHITFORD-LANE</p>
    <p class="cta-phone">
      <svg width="18" height="20" viewBox="0 0 18 20" aria-hidden="true">
        <rect x="0" y="0" width="18" height="20" rx="3" fill="#1f2326"/>
        <path d="M5 4c1 0 1.6 2.4 1.2 3-.4.5-1 .6-.6 1.6.5 1.2 1.6 2.6 2.6 3.2.8.4 1.1-.3 1.6-.6.6-.3 2.7 1 2.7 1.8 0 1.2-1.6 2.2-2.8 2-3-.6-6.8-5.2-6.5-8.6C3.3 5 4.2 4 5 4z" fill="#fff"/>
      </svg>
      0400 555 012
    </p>
    <p class="cta-address">PO Box 118<br>Seacliff Bay NSW 2199</p>
  </section>

  <div class="headshot">
    <div class="headshot-fill" role="img" aria-label="Headshot portrait of the broker, Sam Whitford-Lane"></div>
  </div>
</main>
</body>
</html>
```